Visitenkarten-Design für Immobilienfinanzierer
Zielgruppe
Ich bin hauptsächlich Immobilienfinanzierer. Das bedeutet, dass ich als unabhängiger Finanzmakler für meine Kunden aus über 400 Banken, Versicherungsgesellschaften und Bausparkassen den Finanzierungspartner auswähle, der die beste Kondition anbietet, oder das Projekt überhaupt begleitet. Die durch die Baufinanzierung gewonnenen Kunden berate ich auch zu den Themen Bausparen, Versicherungen, Vermögensanlagen und Privatkredite. Kernthema mit 80% Umsatzanteil ist die Bau/Immobilienfinanzierung. Mitbewerber mit ähnlichem Geschäftsmodell sind hauptsächlich Dr. Wendau, Baveron.
Aufgabenstellung
In meiner Branche ist Seriosität das Maß aller Dinge. Dabei möchte ich eher modern als altbacken auftreten (kein 'Kanzlei'-Design', aber auch nicht zu flippig. Ich bin 40 Jahre alt, und möchte auch mit 60 noch zum Design passen.

```html
<!DOCTYPE html>
<html lang="de">
<head>
<meta charset="utf-8">
<title>Visitenkarte – Veridan</title>
<link rel="stylesheet" href="https://fonts.googleapis.com/css2?family=Questrial&family=Montserrat:wght@600;700&display=swap">
<style>
  :root {
    --stage: #1e1e1e;
    --paper: #ffffff;
    --ink: #333131;
    --ink-soft: #5a5858;
    --green: #9cbf3a;
  }
  * { box-sizing: border-box; margin: 0; padding: 0; }
  html, body { width: 1200px; height: 801px; overflow: hidden; background: var(--stage); }
  .stage {
    position: relative; width: 1200px; height: 801px;
    display: flex; align-items: center; justify-content: center; gap: 60px;
  }
  .card {
    position: relative; width: 520px; height: 336px;
    background: var(--paper); overflow: hidden;
    box-shadow: 0 18px 40px rgba(0,0,0,.45);
  }

  /* Front */
  .front-brand {
    position: absolute; left: 90px; top: 110px;
    display: flex; align-items: center; gap: 18px;
  }
  .brand-dot { width: 64px; height: 64px; border-radius: 50%; background: var(--green); }
  .brand-name {
    font-family: "Montserrat", sans-serif; font-weight: 700;
    font-size: 66px; letter-spacing: 1px; color: var(--ink); line-height: 1;
  }
  .front-web {
    position: absolute; left: 0; right: 0; bottom: 42px;
    display: flex; justify-content: center; align-items: center; gap: 10px;
    font-family: "Montserrat", sans-serif; font-weight: 600;
    font-size: 17px; color: var(--ink); letter-spacing: .5px;
  }

  /* Back */
  .back-mark {
    position: absolute; left: 40px; top: 58px;
    width: 190px; height: 190px; border-radius: 50%; background: var(--green);
  }
  .back-brand {
    position: absolute; left: 160px; bottom: 26px;
    display: flex; align-items: center; gap: 6px;
    font-family: "Questrial", sans-serif; font-size: 20px; color: var(--ink);
  }
  .back-brand .brand-dot { width: 14px; height: 14px; }
  .baseline {
    position: absolute; left: 260px; right: 0; bottom: 36px; height: 5px; background: var(--green);
  }
  .details {
    position: absolute; left: 268px; top: 26px;
    font-family: "Questrial", sans-serif; color: var(--ink-soft);
  }
  .person-name { font-size: 22px; color: var(--ink); }
  .person-role { font-size: 12px; letter-spacing: 1px; color: var(--green); margin-top: 2px; }
  .address { font-size: 13px; line-height: 1.5; margin-top: 26px; }
  .contact-label { font-size: 13px; color: var(--green); margin-top: 26px; }
  .contact-list { list-style: none; font-size: 13px; line-height: 1.75; margin-top: 2px; }
  .icon-tabs {
    position: absolute; right: 0; top: 150px;
    display: flex; flex-direction: column; gap: 6px;
  }
  .icon-tab {
    width: 72px; height: 20px; background: var(--green);
    display: flex; align-items: center; padding-left: 8px;
  }
</style>
</head>
<body>
<main class="stage">
  <section class="card card-front" aria-label="Vorderseite">
    <div class="front-brand">
      <span class="brand-dot"></span>
      <span class="brand-name">Veridan</span>
    </div>
    <p class="front-web">
      <svg width="22" height="22" viewBox="0 0 22 22" fill="none" stroke="#333131" stroke-width="1.4" aria-hidden="true">
        <circle cx="11" cy="11" r="9.5"/><ellipse cx="11" cy="11" rx="4.5" ry="9.5"/>
        <line x1="1.5" y1="11" x2="20.5" y2="11"/><line x1="3" y1="6" x2="19" y2="6"/><line x1="3" y1="16" x2="19" y2="16"/>
      </svg>
      www.klarplanberater.de
    </p>
  </section>

  <section class="card card-back" aria-label="Rückseite">
    <div class="back-mark"></div>
    <div class="baseline"></div>
    <div class="back-brand"><span class="brand-dot"></span>Veridan</div>
    <div class="details">
      <p class="person-name">Marlene Hovestadt</p>
      <p class="person-role">IMMOBILIENFINANZIERER</p>
      <p class="address">Lindenweg 7<br>96199 Ostbach - OT Feldheim</p>
      <p class="contact-label">Kontakt</p>
      <ul class="contact-list">
        <li>00000 / 318 457 6</li>
        <li>00000 / 318 457 5</li>
        <li>info@veridanprivat.de</li>
      </ul>
    </div>
    <div class="icon-tabs" aria-hidden="true">
      <div class="icon-tab">
        <svg width="12" height="12" viewBox="0 0 12 12"><path d="M2.5 1 L4.5 1 L5.3 3.5 L4 4.5 Q5 7 7.5 8 L8.5 6.7 L11 7.5 L11 9.5 Q6 11 1 3 Z" fill="#fff"/></svg>
      </div>
      <div class="icon-tab">
        <svg width="13" height="12" viewBox="0 0 13 12" fill="none" stroke="#fff" stroke-width="1.2"><rect x="1" y="4" width="11" height="6"/><rect x="3.5" y="1" width="6" height="3"/><line x1="3.5" y1="7.5" x2="9.5" y2="7.5"/></svg>
      </div>
      <div class="icon-tab">
        <svg width="13" height="10" viewBox="0 0 13 10" fill="none" stroke="#fff" stroke-width="1.2"><rect x="1" y="1" width="11" height="8"/><polyline points="1,1 6.5,5.5 12,1"/></svg>
      </div>
    </div>
  </section>
</main>
</body>
</html>
```